wedding DJ & Lighting entertainment

We are a DJ and Lighting production company. We specialize mainly in wedding entertainment. I've attached my old postcard in the image folder, however, i would like something new and updated. You can use the same bullet points from the front page, but i would like to have a cleaner look on the front. I'd like to have one large image on the front side and smaller images on the back side. I'd also like to have some text below the logo. I'd like it to say DJ * Lighting * Audio/Visual. I'd also like to have the phrase "Celebrate with Style"

Target Market(s)

weddings, private events, women

Industry/Entity Type

It Company

Font styles to use
Sans Serif
Script

Requirements
Must have
• look elegant, sophisticated. Must have my new logo! My logo is attached as one of the files. It's a headphone logo.

```html
<!DOCTYPE html>
<html lang="en">
<head>
<meta charset="utf-8">
<title>Brightwave Events – Celebrate with Style</title>
<link rel="stylesheet" href="https://fonts.googleapis.com/css2?family=Ubuntu:ital,wght@0,400;0,500;1,700&family=Great+Vibes&display=swap">
<style>
  :root {
    --magenta: #b5338f;
    --plum: #7a3a8e;
    --violet: #6a4aa6;
    --sky: #8fc3e8;
    --gold: #f4c867;
    --peach: #f3a87a;
    --white: #ffffff;
    --ring: #8e6fb8;
  }
  html, body { margin: 0; padding: 0; overflow: hidden; }
  .postcard {
    position: relative;
    width: 1200px;
    height: 800px;
    overflow: hidden;
    background:
      radial-gradient(circle at 78% 10%, rgba(255,232,150,.95) 0, rgba(255,220,140,.55) 14%, transparent 34%),
      radial-gradient(circle at 47% 18%, rgba(170,215,245,.9) 0, rgba(140,190,235,.5) 16%, transparent 36%),
      radial-gradient(circle at 95% 55%, rgba(240,150,200,.7) 0, transparent 30%),
      radial-gradient(circle at 20% 55%, rgba(210,60,160,.85) 0, transparent 45%),
      linear-gradient(120deg, var(--plum) 0%, var(--magenta) 35%, var(--violet) 60%, #9a6fb0 100%);
    font-family: "Ubuntu", sans-serif;
    color: var(--white);
  }
  .deco, .photo-frame { position: absolute; inset: 0; }
  .brand {
    position: absolute;
    left: 52px;
    top: 62px;
    margin: 0;
    font-family: "Ubuntu", sans-serif;
    font-weight: 500;
    font-size: 46px;
    line-height: 1;
    letter-spacing: -1px;
    display: flex;
    align-items: center;
    gap: 12px;
  }
  .brand-dot {
    width: 14px; height: 14px; border-radius: 50%;
    background: var(--white);
  }
  .brand-name { white-space: nowrap; }
  .services-line {
    position: absolute;
    left: 52px;
    top: 166px;
    margin: 0;
    font-family: "Ubuntu", sans-serif;
    font-style: italic;
    font-weight: 700;
    font-size: 30px;
    line-height: 1;
    white-space: nowrap;
  }
  .services-line .sep { font-weight: 400; font-size: 20px; margin: 0 10px; vertical-align: 3px; }
  .tagline {
    position: absolute;
    left: 52px;
    top: 334px;
    margin: 0;
    font-family: "Great Vibes", cursive;
    font-weight: 400;
    font-size: 86px;
    line-height: 1;
    white-space: nowrap;
    transform: rotate(-12deg);
    transform-origin: left bottom;
    text-shadow: 0 2px 6px rgba(60,0,60,.35);
  }
  .tagline .big { font-size: 106px; }
  .feature-list {
    position: absolute;
    left: 0;
    top: 512px;
    margin: 0;
    padding: 0;
    list-style: none;
  }
  .feature {
    width: 354px;
    height: 44px;
    margin-bottom: 8px;
    padding-left: 22px;
    display: flex;
    align-items: center;
    font-size: 24px;
    font-weight: 500;
    background: linear-gradient(90deg, rgba(150,70,170,.85) 0%, rgba(160,120,200,.75) 60%, rgba(150,200,235,.85) 100%);
    border-top: 1px solid rgba(255,255,255,.55);
    border-bottom: 1px solid rgba(255,255,255,.3);
    border-right: 2px solid rgba(255,255,255,.8);
    box-shadow: 0 2px 6px rgba(60,20,80,.25);
  }
</style>
</head>
<body>
<main class="postcard">
  <svg class="deco" width="1200" height="800" viewBox="0 0 1200 800" aria-hidden="true">
    <defs>
      <radialGradient id="sun" cx="50%" cy="50%" r="50%">
        <stop offset="0" stop-color="#fbe7a0" stop-opacity=".9"/>
        <stop offset="1" stop-color="#f4c867" stop-opacity=".45"/>
      </radialGradient>
    </defs>
    <circle cx="1040" cy="70" r="175" fill="url(#sun)"/>
  </svg>

  <svg class="photo-frame" width="1200" height="800" viewBox="0 0 1200 800">
    <defs>
      <radialGradient id="photoTone" cx="45%" cy="55%" r="60%">
        <stop offset="0" stop-color="#e9d8cf"/>
        <stop offset=".35" stop-color="#c7834a"/>
        <stop offset=".75" stop-color="#5a3a4a"/>
        <stop offset="1" stop-color="#2e2236"/>
      </radialGradient>
      <radialGradient id="glow" cx="50%" cy="50%" r="50%">
        <stop offset="0" stop-color="#ffd36a" stop-opacity=".95"/>
        <stop offset="1" stop-color="#f39a5a" stop-opacity=".5"/>
      </radialGradient>
    </defs>
    <circle cx="778" cy="502" r="398" fill="var(--ring)" opacity=".55"/>
    <circle cx="778" cy="502" r="374" fill="url(#photoTone)" role="img"
            aria-label="Photo of a bride and groom sharing their first dance on a wooden floor under string lights, guests watching"/>
    <circle cx="1024" cy="770" r="100" fill="url(#glow)" opacity=".8"/>
  </svg>

  <h1 class="brand">
    <span class="brand-dot"></span>
    <span class="brand-name">Brightwave Events</span>
  </h1>
  <p class="services-line">DJ<span class="sep">|</span>Lighting<span class="sep">|</span>Audio-Visual</p>

  <p class="tagline">Celebrate with <span class="big">Style</span></p>

  <svg class="photo-frame" width="1200" height="800" viewBox="0 0 1200 800" aria-hidden="true">
    <path d="M452 398 C 510 372, 590 356, 682 372" fill="none" stroke="var(--white)" stroke-width="5" stroke-linecap="round"/>
  </svg>

  <ul class="feature-list">
    <li class="feature">DJ &amp; Emcee Entertainment</li>
    <li class="feature">Customized Lighting Decor</li>
    <li class="feature">Event Hosting &amp; Coordination</li>
    <li class="feature">Helpful Planning Tools</li>
    <li class="feature">Personalized Service</li>
  </ul>
</main>
</body>
</html>
```